Eycatcher Flyer
Zielgruppe
Infos auf www.lumawerk-beratung.ch
Lebensberatung, Seminare, persönliche Weiterbildung,Medium
Aufgabenstellung
Suche ein Design für einen coolen, modernen, mystischen exklusiven(Image) Flyer. Format A4 Längs gefaltet (Endformat A5).
Flyer Titel Liebe dein Leben - Liebe dich selbst eventuell auch auf englisch love yourself and celebrates your life
oder vielleicht hat jemand noch einen besseren Slogan Vorschlag
Habe im Anhang ein Dokument mit Text kann ganz oder auszugweise verwendet werden. (Handelt sich um einen ersten Entwurf mögliche Rechtschreibfehler enthalten)
Ansonsten Inputs aus der Hp holen.
Lieblingsfarben Rot,Pink,Giftgrün,Gold,Schwarz, Gelb,

```html
<!DOCTYPE html>
<html lang="de">
<head>
<meta charset="utf-8">
<title>Lumawerk – Liebe Dein Leben Flyer</title>
<link href="https://fonts.googleapis.com/css2?family=Didact+Gothic&family=Open+Sans:wght@400;700&display=swap" rel="stylesheet">
<style>
  :root{
    --pink:#e0157a;
    --pink-soft:#f25aa3;
    --plum:#4a0a2c;
    --plum-deep:#2a0418;
    --ink:#0d0609;
    --paper:#ffffff;
    --grey:#8c8c8c;
    --stage:#ebe8ea;
  }
  *{box-sizing:border-box;margin:0;padding:0}
  html,body{width:1200px;height:929px;overflow:hidden;background:var(--stage)}
  body{font-family:"Didact Gothic",sans-serif;color:var(--paper)}
  .spread{position:absolute;left:280px;width:640px;height:452px;overflow:hidden;background:var(--paper);box-shadow:0 4px 18px rgba(0,0,0,.18)}
  .spread--outside{top:6px}
  .spread--inside{top:470px;background:linear-gradient(135deg,var(--plum-deep),var(--plum) 55%,#6b0d40)}
  .spread svg.shapes{position:absolute;inset:0;width:100%;height:100%}
  .photo{position:absolute;border-radius:50%}
  .photo--orchid{background:radial-gradient(circle at 45% 45%,#f03d9a,#c4126b 55%,rgba(196,18,107,0) 72%)}
  .photo--orchid-spray{background:radial-gradient(ellipse at 50% 50%,#e8509e,#b8175f 50%,rgba(184,23,95,0) 72%)}
  .brand{position:absolute;display:flex;align-items:center;gap:8px;color:var(--plum)}
  .brand__dot{width:22px;height:22px;border-radius:50%;background:var(--pink)}
  .brand__name{font-size:26px;letter-spacing:.5px}
  .brand__tagline{position:absolute;font-size:7px;color:#444;white-space:nowrap}
  .contact{position:absolute;left:86px;top:84px;font-size:7.5px;line-height:1.55;width:140px}
  .contact__brand{display:flex;align-items:center;gap:5px;font-size:13px;margin-bottom:10px}
  .contact__brand i{width:9px;height:9px;border-radius:50%;background:var(--pink);display:block}
  .contact dt{color:var(--pink);float:left;width:34px}
  .contact dd{margin-left:34px}
  .slogan{position:absolute;right:110px;top:338px;text-align:right;line-height:1.05;font-weight:400}
  .slogan__line{display:block;font-size:19px;color:#f7c9df}
  .slogan__line--main{font-size:28px;color:var(--paper)}
  .inside-col{position:absolute;font-family:"Open Sans",sans-serif;font-size:7px;line-height:1.5;color:#ead6e0}
  .inside-col p{margin-bottom:7px}
  .inside-col h2{font-size:9px;color:var(--pink-soft);font-weight:700;margin-bottom:6px;letter-spacing:.5px}
  .questions{position:absolute;left:348px;top:110px;width:118px;font-family:"Open Sans",sans-serif;font-size:7.5px;font-weight:700;line-height:1.45;list-style:none}
  .questions li::before{content:"• "}
  .questions .accent{color:var(--pink-soft)}
  .quote{position:absolute;left:336px;top:278px;width:140px;text-align:center;font-family:"Open Sans",sans-serif;font-weight:700;font-size:9px;line-height:1.4}
  .quote__rule{display:block;height:2px;background:var(--pink);margin:6px 30px}
</style>
</head>
<body>

<section class="spread spread--outside" aria-label="Flyer Aussenseite">
  <svg class="shapes" viewBox="0 0 640 452" aria-hidden="true">
    <defs>
      <linearGradient id="plumFill" x1="0" y1="0" x2="1" y2="1">
        <stop offset="0" stop-color="#2a0418"/>
        <stop offset=".6" stop-color="#4a0a2c"/>
        <stop offset="1" stop-color="#6e0d43"/>
      </linearGradient>
    </defs>
    <path fill="url(#plumFill)" d="M170 0 L320 0 C300 70 320 120 400 128 C520 140 600 210 575 320 C555 410 470 452 400 452 L0 452 L0 300 C80 320 150 290 170 230 C190 170 150 90 170 0 Z"/>
    <path fill="none" stroke="var(--pink)" stroke-width="16" d="M330 0 C305 70 325 118 400 126 C520 138 602 210 577 320 C558 405 478 452 404 452"/>
    <path fill="none" stroke="var(--pink)" stroke-width="14" d="M0 300 C90 330 160 290 200 250 C260 200 340 200 380 220"/>
    <path fill="none" stroke="var(--pink-soft)" stroke-width="8" d="M20 452 C120 400 240 330 330 300"/>
    <path fill="var(--ink)" d="M70 60 C110 30 200 35 225 80 C250 130 235 230 190 250 C140 272 80 250 68 200 C55 150 40 85 70 60 Z"/>
    <path fill="none" stroke="var(--pink)" stroke-width="6" d="M70 60 C110 30 200 35 225 80 C250 130 235 230 190 250"/>
    <line x1="320" y1="0" x2="320" y2="452" stroke="rgba(0,0,0,.08)" stroke-width="1"/>
  </svg>

  <div class="photo photo--orchid-spray" style="left:-20px;top:10px;width:90px;height:170px" role="img" aria-label="Rispe pinker Orchideenblüten am linken Rand"></div>
  <div class="photo photo--orchid" style="left:300px;top:10px;width:130px;height:120px" role="img" aria-label="Pinke Orchideenblüte in Nahaufnahme"></div>
  <div class="photo photo--orchid-spray" style="left:545px;top:170px;width:100px;height:150px" role="img" aria-label="Herabhängende Orchideenrispe am rechten Rand"></div>

  <div class="contact">
    <div class="contact__brand"><i></i>Lumawerk</div>
    <p>Lumawerk<br>9470 Seewil</p>
    <dl style="margin-top:10px">
      <dt>Telefon</dt><dd>079 · 412 37 90</dd>
      <dt>E-Mail</dt><dd>info@lumawerk-beratung.ch</dd>
      <dt>Web</dt><dd>www.lumawerk-beratung.ch</dd>
    </dl>
  </div>

  <div class="brand" style="left:462px;top:92px">
    <span class="brand__name">Lumawerk</span><span class="brand__dot"></span>
  </div>
  <span class="brand__tagline" style="left:540px;top:128px">Der Weg nach innen</span>

  <h1 class="slogan">
    <span class="slogan__line">Liebe Dein Leben</span>
    <span class="slogan__line slogan__line--main">Liebe Dich selbst</span>
  </h1>
</section>

<section class="spread spread--inside" aria-label="Flyer Innenseite">
  <svg class="shapes" viewBox="0 0 640 452" aria-hidden="true">
    <path fill="rgba(255,255,255,.05)" d="M180 0 C260 60 200 200 280 260 C340 310 300 452 300 452 L120 452 C160 360 80 260 140 160 C170 110 150 40 180 0 Z"/>
    <path fill="var(--paper)" d="M500 0 L640 0 L640 452 L470 452 C500 360 470 200 500 0 Z"/>
    <path fill="none" stroke="var(--pink)" stroke-width="6" d="M500 0 C470 200 500 360 470 452"/>
    <path fill="var(--ink)" d="M350 96 C390 70 470 80 478 130 C486 180 450 220 400 215 C350 210 320 130 350 96 Z"/>
  </svg>

  <div class="inside-col" style="left:28px;top:30px;width:140px">
    <h2>LOVE YOUR LIFE</h2>
    <p>Wir erinnern uns oft zu selten daran, wie wertvoll jeder einzelne Tag ist. Im Alltag verlieren wir leicht den Blick für das, was uns wirklich nährt und stärkt.</p>
    <p>Gefühle wie Angst, Zweifel und Unruhe zeigen uns, wo wir hinschauen dürfen. Sie sind Wegweiser zu einem ruhigeren Leben.</p>
  </div>
  <div class="inside-col" style="left:186px;top:46px;width:140px">
    <p>Manchmal wissen wir genau, was wir uns wünschen, und finden doch nicht den ersten Schritt dorthin.</p>
    <p>Wenn du nicht weisst, wo du stehst, helfen dir klare Fragen, deinen eigenen Weg zu erkennen.</p>
    <p>Wenn du dein Ziel kennst, wird jeder Tag leichter und du findest deine Kraft.</p>
  </div>

  <ul class="questions">
    <li>Was habe ich?</li>
    <li class="accent">Was will ich?</li>
    <li>Warum?</li>
    <li class="accent">Was ist mir im Leben wichtig?</li>
    <li>Worauf verzichte ich, wenn ich dieses Ziel erreiche?</li>
  </ul>

  <blockquote class="quote">
    <span class="quote__rule"></span>
    Oft sind wir so damit beschäftigt, jemand oder etwas zu werden, dass wir ganz vergessen, jemand zu sein.
    <span class="quote__rule"></span>
  </blockquote>

  <div class="brand" style="left:512px;top:46px;gap:6px">
    <span class="brand__name" style="font-size:19px">Lumawerk</span><span class="brand__dot" style="width:16px;height:16px"></span>
  </div>
  <span class="brand__tagline" style="left:562px;top:74px;font-size:6px">Der Weg nach innen</span>

  <div class="photo photo--orchid-spray" style="left:500px;top:200px;width:120px;height:190px" role="img" aria-label="Rispe pinker Orchideenblüten"></div>
</section>

</body>
</html>
```